Brochure for community platform NGO needed

We are a non-profit working on building the first community platform for refugees, supporters and organisations all over Europe to facilitate inclusion on a community level.

We need a brochure with nice design to show to other organisations, donors, etc.

The design should show our emphasis on community, participation, humanity and empowerment. It should communicate trustworthiness, optimism and equality.

Target Market(s)

locals and organisations supporting refugees in europe

Industry/Entity Type

Non-Profit

Requirements
Must have
• our logo
Nice to have
• design representing the idea - something with bridges or puzzle pieces, something showing community, diversity, participation, etc.
Should not have
• stereotypical representations

```html
<!DOCTYPE html>
<html lang="en">
<head>
<meta charset="utf-8">
<title>Pontara brochure cover</title>
<link rel="stylesheet" href="https://fonts.googleapis.com/css2?family=Anton&family=Open+Sans:wght@400;700&display=swap">
<style>
  :root {
    --stage: #8f8f8f;
    --paper: #dcdcdc;
    --navy: #1b2a58;
    --gold: #b08f26;
    --charcoal: #433b3c;
    --taupe: #9a8f8f;
    --photo-a: #2a57b8;
    --photo-b: #1d2f66;
    --white: #ffffff;
  }
  html, body {
    margin: 0;
    width: 1200px;
    height: 1172px;
    overflow: hidden;
    background: var(--stage);
  }
  .brochure-cover {
    position: absolute;
    left: 210px;
    top: 35px;
    width: 780px;
    height: 1103px;
    box-shadow: 0 10px 30px rgba(0,0,0,0.35);
  }
  .cover-art { display: block; }
  .paper { fill: var(--paper); }
  .navy { fill: var(--navy); }
  .gold { fill: var(--gold); }
  .charcoal { fill: var(--charcoal); }
  .taupe { fill: var(--taupe); }
  .brand-name {
    font-family: "Open Sans", sans-serif;
    font-weight: 700;
    font-size: 74px;
    fill: var(--navy);
    letter-spacing: 1px;
  }
  .band-label {
    font-family: "Open Sans", sans-serif;
    font-size: 26px;
    fill: var(--paper);
    letter-spacing: 0.5px;
  }
  .contact-email {
    font-family: "Open Sans", sans-serif;
    font-size: 17px;
    fill: var(--white);
  }
  .web-address {
    font-family: "Open Sans", sans-serif;
    font-size: 22px;
    fill: var(--paper);
    letter-spacing: 8px;
  }
  .slogan-small {
    font-family: "Open Sans", sans-serif;
    font-size: 32px;
    fill: var(--navy);
  }
  .slogan-big {
    font-family: "Anton", sans-serif;
    font-size: 96px;
    fill: var(--navy);
  }
</style>
</head>
<body>
<div class="brochure-cover">
  <svg class="cover-art" width="780" height="1103" viewBox="0 0 780 1103">
    <defs>
      <linearGradient id="photoTone" x1="0" y1="0" x2="1" y2="1">
        <stop offset="0" stop-color="#2a57b8"/>
        <stop offset="1" stop-color="#1d2f66"/>
      </linearGradient>
    </defs>

    <rect class="paper" x="0" y="0" width="780" height="1103"/>

    <!-- brand lockup -->
    <circle class="navy" cx="418" cy="118" r="26"/>
    <text class="brand-name" x="760" y="142" text-anchor="end">pontara</text>

    <!-- top navy band -->
    <polygon class="navy" points="420,200 780,200 780,290 470,290"/>

    <!-- left navy bar -->
    <rect class="navy" x="0" y="330" width="40" height="170"/>

    <!-- gold lower field -->
    <polygon class="gold" points="440,670 780,670 780,1103 0,1103 0,930 440,930"/>

    <!-- tall navy column -->
    <polygon class="navy" points="235,360 420,330 470,930 290,930"/>

    <!-- gold community band -->
    <rect class="gold" x="60" y="470" width="360" height="72"/>
    <text class="band-label" x="400" y="516" text-anchor="end">BUILDING COMMUNITY</text>

    <!-- charcoal triangle -->
    <polygon class="charcoal" points="60,542 245,542 290,930"/>

    <!-- taupe wedge -->
    <polygon class="taupe" points="420,290 560,290 440,360"/>

    <!-- photo area -->
    <rect x="440" y="290" width="340" height="330" fill="url(#photoTone)" role="img" aria-label="Photo of a young child drinking from a bottle in front of a blue tent"/>

    <!-- navy strip with email -->
    <rect class="navy" x="440" y="620" width="340" height="50"/>
    <text class="contact-email" x="762" y="652" text-anchor="end">info@pontara.eu</text>

    <!-- navy box under photo -->
    <rect class="navy" x="470" y="670" width="250" height="100"/>
    <rect x="480" y="688" width="240" height="82" fill="none" stroke="var(--gold)" stroke-width="4"/>

    <!-- charcoal box with web address -->
    <rect class="charcoal" x="480" y="785" width="300" height="150"/>
    <text class="web-address" x="766" y="918" text-anchor="end">www.pontara.eu</text>

    <!-- slogan -->
    <text class="slogan-small" x="405" y="1000" text-anchor="end">UNITED</text>
    <text class="slogan-small" x="405" y="1038" text-anchor="end">FOR</text>
    <text class="slogan-big" x="415" y="1040" textLength="345" lengthAdjust="spacingAndGlyphs">HUMANITY</text>
  </svg>
</div>
</body>
</html>
```